I need graphics or illustrations to be used in a book and a power point presentation

I have created nine simple graphics using MS paint that were in blog articles. I now need to put these graphics in a book that I am publishing and also in a power point presentation.

I want these graphics to look more professional and consistent looking.

I have provided a word doc showing these graphics that need to be re-done

```html
<!DOCTYPE html>
<html lang="en">
<head>
<meta charset="utf-8">
<title>The Gentiles – Timeline</title>
<link rel="stylesheet" href="https://fonts.googleapis.com/css2?family=Source+Sans+3:wght@400;600&display=swap">
<style>
  :root {
    --canvas-bg: #ffffff;
    --accent: #1cb5ea;
    --accent-dark: #1590bd;
    --accent-fold: #0f7aa3;
    --ink: #2a2a2a;
    --rule-muted: #b5b5b5;
    --banner-text: #ffffff;
  }
  html, body {
    margin: 0;
    padding: 0;
    overflow: hidden;
    background: var(--canvas-bg);
  }
  .canvas {
    position: relative;
    width: 1200px;
    height: 720px;
    overflow: hidden;
    background: var(--canvas-bg);
    font-family: "Source Sans 3", "Myriad Pro", Arial, sans-serif;
    color: var(--ink);
  }
  .title-ribbon {
    position: absolute;
    left: 0;
    top: 0;
    width: 1200px;
    height: 300px;
  }
  .ribbon-tail { fill: var(--accent); }
  .ribbon-fold { fill: var(--accent-fold); }
  .ribbon-face { fill: var(--accent); }
  .ribbon-title {
    position: absolute;
    left: 329px;
    top: 117px;
    width: 541px;
    height: 78px;
    margin: 0;
    display: flex;
    align-items: center;
    justify-content: center;
    font-size: 35px;
    font-weight: 400;
    color: var(--banner-text);
  }
  .timeline-graphic {
    position: absolute;
    left: 0;
    top: 0;
    width: 1200px;
    height: 720px;
  }
  .timeline-axis { stroke: var(--accent); stroke-width: 3; }
  .timeline-endpoint { fill: var(--accent); }
  .event-marker {
    stroke: var(--rule-muted);
    stroke-width: 2;
    stroke-dasharray: 6 5;
  }
  .year-label {
    position: absolute;
    top: 326px;
    margin: 0;
    font-size: 31px;
    font-weight: 400;
    color: var(--ink);
    transform: translateX(-50%);
  }
  .era-label {
    position: absolute;
    left: 692px;
    top: 333px;
    margin: 0;
    font-size: 23px;
    color: var(--accent);
    transform: translateX(-50%);
    white-space: nowrap;
  }
  .event-label {
    position: absolute;
    top: 513px;
    margin: 0;
    font-size: 19px;
    line-height: 1.4;
    color: var(--ink);
  }
</style>
</head>
<body>
<div class="canvas">
  <svg class="title-ribbon" viewBox="0 0 1200 300" aria-hidden="true">
    <polygon class="ribbon-tail" points="251,162 380,162 380,250 251,250 290,206"/>
    <polygon class="ribbon-tail" points="949,162 820,162 820,250 949,250 910,206"/>
    <polygon class="ribbon-fold" points="329,195 380,195 380,250"/>
    <polygon class="ribbon-fold" points="871,195 820,195 820,250"/>
    <rect class="ribbon-face" x="329" y="117" width="542" height="78"/>
  </svg>
  <h1 class="ribbon-title">The Gentiles</h1>

  <svg class="timeline-graphic" viewBox="0 0 1200 720" aria-hidden="true">
    <line class="timeline-axis" x1="112" y1="393" x2="1083" y2="393"/>
    <circle class="timeline-endpoint" cx="112" cy="393" r="14"/>
    <circle class="timeline-endpoint" cx="1083" cy="393" r="14"/>
    <line class="event-marker" x1="112" y1="412" x2="112" y2="505"/>
    <line class="event-marker" x1="575" y1="398" x2="575" y2="505"/>
    <line class="event-marker" x1="893" y1="398" x2="893" y2="505"/>
  </svg>

  <p class="year-label" style="left:112px">1834</p>
  <p class="year-label" style="left:1083px">1836</p>
  <p class="era-label">Dispensation of the “Last Times”</p>

  <p class="event-label" style="left:106px">High Priest doubt and<br>reject the fulness</p>
  <p class="event-label" style="left:522px">Consecration<br>Failure</p>
  <p class="event-label" style="left:837px">Name Change<br>of the Church</p>
</div>
</body>
</html>
```